Curtain Cleaning Flyer to be designed for Singapore market

We are a laundry company providing curtain cleaning services to Singapore market. We have a company vehicle pickup and provide dismantling of curtain at customer house. The dismantled curtain will be weighed and quote will be given to customer immediately. If they accept the price, we will delivered and installed the clean curtain to them.
Refer to our website for more information https://www.glintora.com.sg/curtain-cleaning
The flyer will be distributed to higher income level people in Singapore staying in condominium/semi detached or bungalow.
I need a well designed flyers to engage people to use my service. So please help.

Target Market(s)

Singapore market

Industry/Entity Type

It Company

Requirements
Must have
• MUST INCLUDE CURTAINS pictures in design to let people know it is for curtain laundry
• 1) Flyer has to be eye catching and engage people to call and use our curtain cleaning services.
• 2) It has to professional.
• 3) It has to provide clear information of the following (see curtain cleaning picture I have provided)
• Curtain Laundry at $10/kg
• Call 8362 4915
• No Hidden Cost
• Include Pickup, Dismantle, Installation and Delivery
• 4) Provide company information:
• KORU FLINT, Reg No.71846302K
• 47 Merrowby Lane
• Singapore 071934
• https://www.glintora.com.sg/curtain-cleaning
• Email: enquiries@glintora.com.sg
• Tel: +65 8362 4915
• 5) Include our company logo but do not use it extensively.
Nice to have
• Nice to have a compelling action design for people to call and use my service.
• Nice to highlight on the good laundry price $10 per kg for curtain laundry
• Nice to be professional and cute
Should not have
• Complicated
• No design on woman wearing low cut dresses for promotion

```html
<!DOCTYPE html>
<html lang="en">
<head>
<meta charset="utf-8">
<title>Koru Flint Curtain Laundry Flyer</title>
<link rel="stylesheet" href="https://fonts.googleapis.com/css2?family=Londrina+Solid:wght@900&family=Oswald:wght@600&family=Open+Sans:wght@400;600;700&display=swap">
<style>
  :root {
    --brand-blue: #1a72b9;
    --sky-blue: #16b2e8;
    --sky-blue-dark: #0e96cf;
    --ink: #333333;
    --grey-band: #6e6f71;
    --grey-swoosh: #b4b5b7;
    --paper: #ffffff;
    --photo-light: #f1ece1;
    --photo-mid: #d9d2c2;
    --photo-dark: #9b9790;
  }
  * { margin: 0; padding: 0; box-sizing: border-box; }
  html, body { width: 967px; height: 1200px; overflow: hidden; background: var(--paper); }
  .flyer { position: relative; width: 967px; height: 1200px; background: var(--paper); font-family: "Open Sans", sans-serif; }
  .hero { position: absolute; left: 0; top: 0; width: 967px; height: 680px; }
  .price-badge {
    position: absolute; left: 652px; top: 380px; width: 272px; height: 272px; border-radius: 50%;
    background: var(--paper); box-shadow: 0 6px 14px rgba(0,0,0,.35);
  }
  .price-badge__disc {
    position: absolute; inset: 10px; border-radius: 50%; overflow: hidden;
    background: radial-gradient(circle at 40% 35%, #2cc2f2, var(--sky-blue) 60%, var(--sky-blue-dark));
    display: flex; align-items: center; justify-content: center;
  }
  .price-badge__text { font-family: "Oswald", sans-serif; font-weight: 600; font-size: 70px; color: #fff; letter-spacing: -1px; margin-top: -18px; }
  .price-badge__peel { position: absolute; right: 0; bottom: 0; }
  .headline {
    position: absolute; top: 672px; width: 100%; text-align: center;
    font-family: "Londrina Solid", sans-serif; font-weight: 900; font-size: 86px; line-height: 1;
    color: var(--brand-blue); letter-spacing: 1px;
  }
  .brand {
    position: absolute; top: 780px; width: 100%; display: flex; justify-content: center; align-items: center; gap: 12px;
    font-weight: 700; font-size: 34px; color: var(--sky-blue); letter-spacing: 1px;
  }
  .brand__dot { width: 22px; height: 22px; border-radius: 50%; background: var(--sky-blue); }
  .includes-title {
    position: absolute; top: 850px; width: 100%; text-align: center;
    font-family: "Londrina Solid", sans-serif; font-weight: 900; font-size: 30px; color: var(--brand-blue);
  }
  .services { position: absolute; top: 904px; left: 0; width: 100%; display: flex; justify-content: center; gap: 20px; }
  .service {
    width: 104px; height: 104px; border-radius: 50%; background: #e6e7e8;
    box-shadow: 0 3px 6px rgba(0,0,0,.25); padding: 5px;
  }
  .service__disc {
    width: 100%; height: 100%; border-radius: 50%;
    background: radial-gradient(circle at 45% 35%, #36c4f3, var(--sky-blue) 60%, var(--sky-blue-dark));
    display: flex; flex-direction: column; align-items: center; padding-top: 16px;
  }
  .service__label { font-size: 9.5px; font-weight: 700; color: #fff; letter-spacing: .2px; }
  .service__icon { margin-top: 4px; }
  .services-shadow {
    position: absolute; top: 1010px; left: 230px; width: 507px; height: 18px; border-radius: 50%;
    background: radial-gradient(ellipse at center, rgba(0,0,0,.18), rgba(0,0,0,0) 70%);
  }
  .no-hidden-cost { position: absolute; top: 1026px; width: 100%; text-align: center; font-weight: 700; font-size: 27px; color: var(--brand-blue); }
  .call { position: absolute; top: 1062px; width: 100%; display: flex; justify-content: center; align-items: center; gap: 12px; }
  .call__number { font-weight: 700; font-size: 50px; color: var(--ink); letter-spacing: .5px; }
  .contact-bar {
    position: absolute; left: 0; bottom: 0; width: 100%; height: 76px; background: var(--grey-band);
    display: flex; align-items: center; justify-content: center; gap: 28px; color: #fff; font-size: 17px;
  }
  .contact-bar__item { display: flex; align-items: center; gap: 8px; }
  .contact-bar::before { content: ""; position: absolute; left: 0; top: -6px; width: 100%; height: 6px; background: #e9e9ea; }
</style>
</head>
<body>
<main class="flyer">
  <svg class="hero" viewBox="0 0 967 680" xmlns="http://www.w3.org/2000/svg">
    <defs>
      <linearGradient id="photoTone" x1="0" y1="0" x2="1" y2="1">
        <stop offset="0" stop-color="var(--photo-light)"/>
        <stop offset=".5" stop-color="var(--photo-mid)"/>
        <stop offset="1" stop-color="var(--photo-dark)"/>
      </linearGradient>
    </defs>
    <path d="M0 565 C90 615 220 660 390 665 C600 670 820 590 967 530 V0 H0 Z" fill="var(--grey-swoosh)"/>
    <path d="M0 548 C90 592 220 632 390 636 C600 640 820 570 967 512 V0 H0 Z" fill="#e4e4e5"/>
    <path role="img" aria-label="Photo of cream patterned curtains drawn back from a garden window, with a grey armchair and white cushions" d="M0 540 C90 584 220 622 390 626 C600 630 820 560 967 500 V0 H0 Z" fill="url(#photoTone)"/>
  </svg>

  <div class="price-badge">
    <div class="price-badge__disc">
      <span class="price-badge__text">$10/kg</span>
      <svg class="price-badge__peel" width="120" height="120" viewBox="0 0 120 120">
        <path d="M120 30 C95 70 70 100 30 120 L120 120 Z" fill="#fff"/>
        <path d="M120 30 C110 70 90 85 30 120 C60 80 80 60 120 30 Z" fill="#aee6fa"/>
      </svg>
    </div>
  </div>

  <h1 class="headline">CURTAIN LAUNDRY</h1>

  <div class="brand"><span class="brand__dot"></span><span>KORU FLINT</span></div>

  <h2 class="includes-title">INCLUDES</h2>

  <ul class="services" style="list-style:none">
    <li class="service"><div class="service__disc">
      <span class="service__label">PICKUP</span>
      <svg class="service__icon" width="40" height="42" viewBox="0 0 40 42" fill="none" stroke="#fff" stroke-width="3" stroke-linecap="round">
        <path d="M6 4 L14 6 L18 34 L34 32"/><circle cx="18" cy="37" r="3.5" fill="#fff"/>
        <rect x="19" y="12" width="13" height="16" fill="#fff" stroke="none"/>
      </svg>
    </div></li>
    <li class="service"><div class="service__disc">
      <span class="service__label">DISMANTLE</span>
      <svg class="service__icon" width="42" height="42" viewBox="0 0 42 42" fill="none" stroke="#fff" stroke-width="4" stroke-linecap="round">
        <path d="M8 34 L32 10"/><path d="M28 6 a7 7 0 1 0 8 8"/><path d="M10 8 L34 34"/>
      </svg>
    </div></li>
    <li class="service"><div class="service__disc">
      <span class="service__label">INSTALLATION</span>
      <svg class="service__icon" width="42" height="42" viewBox="0 0 42 42">
        <circle cx="16" cy="26" r="10" fill="none" stroke="#fff" stroke-width="6" stroke-dasharray="4 3"/>
        <circle cx="16" cy="26" r="4" fill="#fff"/>
        <circle cx="31" cy="11" r="6" fill="none" stroke="#fff" stroke-width="4" stroke-dasharray="3 2"/>
      </svg>
    </div></li>
    <li class="service"><div class="service__disc">
      <span class="service__label">DELIVERY</span>
      <svg class="service__icon" width="54" height="40" viewBox="0 0 54 40" fill="#fff">
        <rect x="2" y="6" width="32" height="22"/><path d="M36 12 H46 L52 20 V28 H36 Z"/>
        <circle cx="12" cy="31" r="5" stroke="#16b2e8" stroke-width="2"/><circle cx="44" cy="31" r="5" stroke="#16b2e8" stroke-width="2"/>
      </svg>
    </div></li>
  </ul>
  <div class="services-shadow"></div>

  <p class="no-hidden-cost">NO HIDDEN COST</p>

  <div class="call">
    <svg width="46" height="46" viewBox="0 0 46 46" fill="none">
      <path d="M8 6 L16 4 L20 14 L15 18 C18 25 22 29 28 32 L32 27 L42 31 L40 39 C26 42 6 24 8 6 Z" fill="var(--ink)"/>
      <path d="M26 8 a12 12 0 0 1 12 12 M26 2 a18 18 0 0 1 18 18" stroke="var(--sky-blue)" stroke-width="3" stroke-linecap="round"/>
    </svg>
    <span class="call__number">8362 4915</span>
  </div>

  <footer class="contact-bar">
    <span class="contact-bar__item">
      <svg width="13" height="18" viewBox="0 0 13 18"><path d="M6.5 0 C2.9 0 0 2.8 0 6.3 C0 11 6.5 18 6.5 18 S13 11 13 6.3 C13 2.8 10.1 0 6.5 0 Z M6.5 8.8 a2.5 2.5 0 1 1 0-5 a2.5 2.5 0 0 1 0 5 Z" fill="#fff"/></svg>
      47 Merrowby Lane Singapore 071934
    </span>
    <span class="contact-bar__item">
      <svg width="20" height="14" viewBox="0 0 20 14" fill="none" stroke="#fff" stroke-width="1.6"><rect x="1" y="1" width="18" height="12"/><path d="M1 1 L10 8 L19 1"/></svg>
      enquiries@glintora.com.sg
    </span>
    <span class="contact-bar__item">
      <svg width="18" height="18" viewBox="0 0 18 18" fill="none" stroke="#fff" stroke-width="1.4"><circle cx="9" cy="9" r="8"/><ellipse cx="9" cy="9" rx="3.5" ry="8"/><path d="M1 9 H17 M2.5 5 H15.5 M2.5 13 H15.5"/></svg>
      www.glintora.com.sg
    </span>
  </footer>
</main>
</body>
</html>
```